Mortgage Broking boutique Business

I’m wanting a revamped look to my existing business card design. I do like the black and silver but happy to have other colours introduced based on your creation. I’ve attached a copy of my current card so you can have a starting point updated details noted brloe. I deal with high net worth individuals so need my card to be sophisticated, classy that gives off a classy vibe

Target Market(s)

High net worth, wealthy

Industry/Entity Type

Mortgage Brokerage

Contact Information for Business Card

Job title: Finance Executive
Phone: +61 7 3287 4419
Mobile: 0471 352 608
Email: marcus@quillbrookcapital.com.au
Web: www.quillbrookcapital.com.au
Address: level 36 Tindale Court, 58 Harwick St Brisbane QLD 4000

Font styles to use
Other font styles liked:
• Helvetica

Colors

Designer to choose colors to be used in the design.

Requirements
Must have
• Use my existing card design as a starting point

```html
<!DOCTYPE html>
<html lang="en">
<head>
<meta charset="utf-8">
<title>Quillbrook Capital – Business Card</title>
<link rel="stylesheet" href="https://fonts.googleapis.com/css2?family=Arimo:wght@400&display=swap">
<style>
  :root {
    --backdrop: #625e58;
    --card-deep: #050505;
    --card-sheen: #2a2a2a;
    --silver-light: #e6e6e6;
    --silver-mid: #9a9a9a;
    --silver-dark: #5c5c5c;
    --ink-light: #f0f0f0;
    --ink-soft: #dcdcdc;
    --wordmark: #c9c9c9;
  }
  * { margin: 0; padding: 0; box-sizing: border-box; }
  html, body {
    width: 1200px; height: 960px; overflow: hidden;
    background: var(--backdrop);
    font-family: "Arimo", Helvetica, Arial, sans-serif;
  }
  .canvas { position: relative; width: 1200px; height: 960px; }

  .card {
    position: absolute;
    width: 716px; height: 393px;
    background: linear-gradient(100deg, var(--card-deep) 0%, #101010 35%, var(--card-sheen) 50%, #101010 62%, var(--card-deep) 100%);
    box-shadow: 0 8px 14px rgba(0,0,0,0.35);
  }
  .card--front { left: 242px; top: 79px; }
  .card--back  { left: 245px; top: 505px; }

  .card__frame {
    position: absolute; inset: 20px;
    border: 3px solid transparent;
    border-image: linear-gradient(100deg, var(--silver-dark), var(--silver-light) 30%, var(--silver-mid) 55%, var(--silver-light) 80%, var(--silver-dark)) 1;
  }

  .wordmark {
    position: absolute; left: 0; right: 0; top: 148px;
    text-align: center;
    color: var(--wordmark);
    font-size: 34px; font-weight: 400;
    letter-spacing: 0.42em;
    line-height: 47px;
    padding-left: 0.42em;
  }

  .holder__name {
    position: absolute; left: 0; right: 0; top: 88px;
    text-align: center; color: var(--ink-light);
    font-size: 37px; font-weight: 400; letter-spacing: 0.01em;
  }
  .holder__title {
    position: absolute; left: 0; right: 0; top: 145px;
    text-align: center; color: var(--ink-soft);
    font-size: 21px;
  }

  .contact__phones {
    position: absolute; right: 387px; top: 211px;
    text-align: right; color: var(--ink-light);
  }
  .contact__office { font-size: 26px; line-height: 32px; display: block; }
  .contact__mobile { font-size: 21px; line-height: 30px; display: block; }

  .contact__divider {
    position: absolute; left: 347px; top: 209px;
    width: 0; height: 94px;
    border-left: 2px dotted var(--silver-mid);
  }

  .contact__details {
    position: absolute; left: 361px; top: 215px;
    color: var(--ink-soft);
  }
  .contact__email { font-size: 17.5px; display: block; }
  .contact__address { font-size: 15.5px; line-height: 19px; display: block; margin-top: 22px; }

  .contact__web {
    position: absolute; left: 0; right: 0; top: 329px;
    text-align: center; color: var(--ink-soft);
    font-size: 14.5px;
  }
</style>
</head>
<body>
<main class="canvas">
  <section class="card card--front" aria-label="Card front">
    <div class="card__frame"></div>
    <div class="wordmark">QUILLBROOK<br>CAPITAL</div>
  </section>

  <section class="card card--back" aria-label="Card back">
    <div class="card__frame"></div>
    <h1 class="holder__name">MARCUS WHITLEY</h1>
    <p class="holder__title">Finance Executive</p>

    <p class="contact__phones">
      <span class="contact__office">+61 7 3287 4419</span>
      <span class="contact__mobile">M: 0471 352 608</span>
    </p>
    <div class="contact__divider"></div>
    <p class="contact__details">
      <span class="contact__email">E: marcus@quillbrookcapital.com.au</span>
      <span class="contact__address">A: level 36 Tindale Court, 58 Harwick<br>St Brisbane QLD 4000</span>
    </p>
    <p class="contact__web">www.quillbrookcapital.com.au</p>
  </section>
</main>
</body>
</html>
```